Football (soccer) board game app design

Hi,

We are a start up looking for a gameplay design for an app. It is a football trivia app that consists of four main screens; login/register, main navigation, gameplay, question.

OVERALL:
We want our app to be kept in a dark theme. Black or very dark gray is preferable, with a couple of nice colors to give it a stylish touch. We like flat designs, but are open for ideas within the general structure design. The logo can be used in the app, but feel free to improve it you feel you can. In the attached material we have tried to outline some of our ideas and other designs friends have helped us make.

LOGIN/REGISTER:
We want a simple login. Email, password, Chatterly login and the possibility to register a new user. Live search check whether the email is valid and free, and there is also live validation of passwords. If this could be incorporated in the design it would be nice.

MAIN NAVIGATION:
In the main navigation screen we want it to be divided into tabs. A home, my games, my categories and a ranking tab. In the top bar it should be possible to search for categories as well as there should be a button to go to settings.

The Home tab
In the home tab we want a "Quick Play" button, and a list of featured categories. A category can be unlocked or locked, which should be illustrated somehow. When a category is tapped it should divide the block into a left and right tap area, where the user can choose to "Beat to unlock" or "Buy to unlock" if locked and "Practice" or "Challenge Friend" if already unlocked.

The My Games tab
In the my games tab, the current games should be divided into three lists. First "your turn", then "opponents turn" and finally "finished games".

The My Categories tab
This tab should include a list of categories, which the user have bought, but as of design it is fairly similar to the blocks in home tab. So not much different here.

The Ranking tab
Ranking should show a set of leaderboards; Today, This Week, This Month, etc. The row in a leaderboard should have teamname and a win percentage.

GAMEPLAY:
The gameplay is inspired by an old football (soccer) board game from the 1950's, and our gameplay consists of three core elements; a football (soccer) pitch, 11 players and a scoreboard.

The football (soccer) pitch
What we need is a pitch seen from behind the goal line. The important issue here, is the perspective, as we want 11 players on the field formed as a 4-3-3 formation, being 1 goalkeeper, 4 defenders, 3 midfielder and 3 strikers. They should all be touchable without overlap. In the other end we want a goal that should be touchable as well. The goal in the nearest end do not have to be visible. Due to the perspective of the field and the fact that players and goal should be touchable, of course give you the opportunity to play around with the proportions of both players and goal. We rather want a large goal being out of proportions, than a small goal with a tiny tap area. Around the field (sidelines and beside the goal) we would like advertising banners like seen on a real stadium.

The players
As mentioned we want 11 players in a 4-3-3 formation. The players should be attached to the board with springs as seen on some of the very old board games, where you could flick the player to pass the ball. This also means that we want the players to be placed in an indentation for the ball to fall into and it would be very cool if you could illustrate the player with the ball, as being pulled back to one of the sides, just enough to see the ball at his feet. The players should be large enough for a user to tap them, hence it would also be beneficial if they are not overlapping. For a start we would like to see the players in a blue shirt and white shorts (socks are not necessary as they are placed on a spring).

Scoreboard
On the scoreboard above the field, we need information such as the names of the two teams (could be FC Brightmoor and Tall Oak Rovers), the score (2-1), minutes played (42), and which half (1st). We also want a progress bar that illustrates how many moves you have used ranging from 0-5. The scoreboard could be inspired from the ones seen around stadiums across the world, but feel free to improvise.

What We Are Looking for
We are looking for full PSD and AI files so we can use them to make minor changes like colors on shirts and shorts, colors on pitch, etc. We really want you to be innovative and inspire us, as we are not designers ourselves. In the attached files, we have tried to sketch out a design that covers our initial ideas. We are looking for a professional look, and having the players and field look like a real board game would just be awesome. A combination of the look from the realistic pitch with advertising banners around it, the idea of our spring-players and the initial thoughts of a design illustrated in our sketch, should help you along. Flat design, cartoonish or somewhere in between is up to you, we just want you to impress and make "wow"-feeling.

QUESTION:
The final screen should display a question with four possible answers. There should be a green/checkmark when correct answer, and a red/cross if incorrect.

That's all. We are looking very much forward to see your designs!
Updates

Hi all,

We have changed the terms of the contest to now have a guaranteed payment, and we are really looking forward to see your designs! Good luck.

/ Mikkel and Anders

By request we have now uploaded an AI-file with the logo for you to play around with. We are looking forward to see your designs.

/ Mikkel and Anders

Reason: Hi designers, We are really happy with the progress being made, and are looking forward to see some of the designs that are still work in progress. However the amount of designs received, has not reached our expectations yet. Therefore we are extending the deadline for seven more days, so designers, that are still working on their designs can continue their work without a stressing deadline in the horizon. Good luck to all of you. We are looking very much forward to see, what you are able to produce. Best regards, Mikkel and Anders

Reason: Hi all, We still have a lot of designers in the competition , who are battling to finish their designs, therefore we have decided to extend the deadline once more. Good luck to all of you!

Target Market(s)

Football (soccer) fans

Industry/Entity Type

Advertising

```html
<!DOCTYPE html>
<html lang="en">
<head>
<meta charset="utf-8">
<title>goalmind – login screens</title>
<link rel="stylesheet" href="https://fonts.googleapis.com/css2?family=Arimo:wght@400;700&family=Raleway:wght@200&display=swap">
<style>
  :root {
    --page: #ffffff;
    --status: #2b2b2b;
    --status-text: #e6e6e6;
    --wood-dark-1: #2a2a2a;
    --wood-dark-2: #1c1c1c;
    --wood-low-1: #3e3e3e;
    --wood-low-2: #2c2c2c;
    --band: #555555;
    --band-edge: rgba(255,255,255,0.22);
    --field: #141414;
    --field-edge: #0a0a0a;
    --field-text: #b4b4b4;
    --icon: #4a4a4a;
    --welcome: #8c8c8c;
    --check-ring: #5e5e5e;
    --check-core: #262626;
    --check-tick: #9a9a9a;
    --social: #3d5587;
    --social-mark: #22355c;
    --white: #ffffff;
  }
  * { box-sizing: border-box; margin: 0; padding: 0; }
  html, body { width: 1200px; height: 588px; overflow: hidden; background: var(--page); }
  body { position: relative; font-family: "Arimo", Arial, sans-serif; }

  .screen {
    position: absolute; width: 320px; height: 480px; overflow: hidden;
    transform-origin: 0 0; transform: scale(1.07);
    background: linear-gradient(180deg, var(--wood-low-1), var(--wood-low-2));
  }
  .screen--email { left: 34px; top: 28px; }
  .screen--login { left: 427px; top: 30px; }
  .screen--register { left: 822px; top: 36px; }

  .wood-top {
    position: absolute; left: 0; top: 0; width: 100%;
    background: linear-gradient(180deg, var(--wood-dark-1), var(--wood-dark-2));
  }
  .status-bar {
    position: absolute; left: 0; top: 0; width: 100%; height: 20px;
    background: var(--status); color: var(--status-text);
    font: 700 13px "Arimo", Arial, sans-serif; text-align: center; line-height: 20px;
  }
  .status-bar .signal { position: absolute; left: 6px; top: 6px; }
  .status-bar .battery { position: absolute; right: 6px; top: 6px; }

  .brand {
    position: absolute; left: 0; width: 100%; text-align: center;
    font: 200 40px "Raleway", Helvetica, sans-serif; color: var(--white); letter-spacing: 1px;
  }

  .form-band {
    position: absolute; left: 0; width: 100%;
    background: var(--band);
    border-top: 1px solid var(--band-edge); border-bottom: 1px solid var(--band-edge);
  }
  .welcome {
    position: absolute; left: 0; width: 100%; text-align: center;
    color: var(--welcome); font-size: 18px;
  }
  .field {
    position: absolute; height: 40px; background: var(--field);
    border: 1px solid var(--field-edge); border-radius: 2px;
    color: var(--field-text); font-size: 14px; line-height: 38px;
  }
  .field svg { position: absolute; left: 9px; top: 7px; }
  .field span { position: absolute; left: 46px; }
  .field--password span { left: 48px; letter-spacing: 1px; }

  .check { position: absolute; width: 64px; height: 64px; }

  .social-login {
    position: absolute; height: 37px; width: 207px;
    background: var(--social); border-radius: 2px;
    color: var(--white); font-size: 14px; line-height: 37px;
  }
  .social-login .mark {
    position: absolute; left: 8px; top: 5px; width: 27px; height: 27px;
    background: var(--social-mark); border-radius: 2px;
  }
  .social-login span { position: absolute; left: 50px; }
</style>
</head>
<body>

<!-- Step 1: email entry -->
<section class="screen screen--email">
  <div class="wood-top" style="height:185px" role="img" aria-label="Dark wood grain backdrop"></div>
  <div class="status-bar">
    <svg class="signal" width="18" height="8"><rect x="0" y="5" width="2" height="3" fill="#ddd"/><rect x="4" y="3" width="2" height="5" fill="#ddd"/><rect x="8" y="2" width="2" height="6" fill="#ddd"/><rect x="12" y="0" width="2" height="8" fill="#ddd"/><rect x="16" y="0" width="2" height="8" fill="#ddd"/></svg>
    9:00 AM
    <svg class="battery" width="20" height="9"><rect x="0.5" y="0.5" width="17" height="8" fill="none" stroke="#ddd"/><rect x="2" y="2" width="14" height="5" fill="#ddd"/><rect x="18" y="3" width="2" height="3" fill="#ddd"/></svg>
  </div>
  <div class="brand" style="top:45px">goalmind</div>
  <div class="form-band" style="top:185px;height:123px" role="img" aria-label="Lighter grey wood band"></div>
  <div class="field" style="left:13px;top:226px;width:295px">
    <svg width="28" height="24" viewBox="0 0 28 24"><rect x="1" y="4" width="26" height="17" fill="none" stroke="var(--icon)" stroke-width="2"/><path d="M1 4 L14 14 L27 4" fill="none" stroke="var(--icon)" stroke-width="2"/></svg>
    <span style="left:54px">Email</span>
  </div>
  <div class="social-login" style="left:57px;top:407px"><i class="mark"></i><span>Login with Chatterly</span></div>
</section>

<!-- Step 2: login -->
<section class="screen screen--login">
  <div class="wood-top" style="height:145px" role="img" aria-label="Dark wood grain backdrop"></div>
  <div class="status-bar">
    <svg class="signal" width="18" height="8"><rect x="0" y="5" width="2" height="3" fill="#ddd"/><rect x="4" y="3" width="2" height="5" fill="#ddd"/><rect x="8" y="2" width="2" height="6" fill="#ddd"/><rect x="12" y="0" width="2" height="8" fill="#ddd"/><rect x="16" y="0" width="2" height="8" fill="#ddd"/></svg>
    9:00 AM
    <svg class="battery" width="20" height="9"><rect x="0.5" y="0.5" width="17" height="8" fill="none" stroke="#ddd"/><rect x="2" y="2" width="14" height="5" fill="#ddd"/><rect x="18" y="3" width="2" height="3" fill="#ddd"/></svg>
  </div>
  <div class="brand" style="top:42px">goalmind</div>
  <div class="form-band" style="top:145px;height:176px" role="img" aria-label="Lighter grey wood band"></div>
  <div class="welcome" style="top:160px">Welcome</div>
  <div class="field" style="left:21px;top:192px;width:255px">
    <svg width="28" height="24" viewBox="0 0 28 24"><rect x="1" y="4" width="26" height="17" fill="none" stroke="var(--icon)" stroke-width="2"/><path d="M1 4 L14 14 L27 4" fill="none" stroke="var(--icon)" stroke-width="2"/></svg>
    <span>anders@postly.net</span>
  </div>
  <div class="field field--password" style="left:21px;top:237px;width:255px">
    <svg width="20" height="26" viewBox="0 0 20 26"><circle cx="10" cy="7" r="6" fill="var(--icon)"/><circle cx="10" cy="6" r="2" fill="var(--field)"/><rect x="8" y="12" width="4" height="13" fill="var(--icon)"/><rect x="12" y="18" width="3" height="2" fill="var(--icon)"/><rect x="12" y="22" width="3" height="2" fill="var(--icon)"/></svg>
    <span>********</span>
  </div>
  <svg class="check" style="left:251px;top:231px" viewBox="0 0 64 64" role="img" aria-label="Submit">
    <circle cx="32" cy="32" r="31" fill="var(--check-ring)"/><circle cx="32" cy="32" r="24" fill="var(--check-core)"/>
    <path d="M20 33 L29 42 L45 21" fill="none" stroke="var(--check-tick)" stroke-width="6" stroke-linecap="round" stroke-linejoin="round"/>
  </svg>
  <div class="social-login" style="left:57px;top:406px"><i class="mark"></i><span>Login with Chatterly</span></div>
</section>

<!-- Step 3: register -->
<section class="screen screen--register">
  <div class="wood-top" style="height:143px" role="img" aria-label="Dark wood grain backdrop"></div>
  <div class="status-bar">
    <svg class="signal" width="18" height="8"><rect x="0" y="5" width="2" height="3" fill="#ddd"/><rect x="4" y="3" width="2" height="5" fill="#ddd"/><rect x="8" y="2" width="2" height="6" fill="#ddd"/><rect x="12" y="0" width="2" height="8" fill="#ddd"/><rect x="16" y="0" width="2" height="8" fill="#ddd"/></svg>
    9:00 AM
    <svg class="battery" width="20" height="9"><rect x="0.5" y="0.5" width="17" height="8" fill="none" stroke="#ddd"/><rect x="2" y="2" width="14" height="5" fill="#ddd"/><rect x="18" y="3" width="2" height="3" fill="#ddd"/></svg>
  </div>
  <div class="brand" style="top:42px">goalmind</div>
  <div class="form-band" style="top:143px;height:207px" role="img" aria-label="Lighter grey wood band"></div>
  <div class="welcome" style="top:160px">Welcome</div>
  <div class="field" style="left:18px;top:192px;width:265px">
    <svg width="28" height="24" viewBox="0 0 28 24"><rect x="1" y="4" width="26" height="17" fill="none" stroke="var(--icon)" stroke-width="2"/><path d="M1 4 L14 14 L27 4" fill="none" stroke="var(--icon)" stroke-width="2"/></svg>
    <span style="left:52px">anders@postly.net</span>
  </div>
  <div class="field field--password" style="left:20px;top:238px;width:263px">
    <svg width="20" height="26" viewBox="0 0 20 26"><circle cx="10" cy="7" r="6" fill="var(--icon)"/><circle cx="10" cy="6" r="2" fill="var(--field)"/><rect x="8" y="12" width="4" height="13" fill="var(--icon)"/><rect x="12" y="18" width="3" height="2" fill="var(--icon)"/><rect x="12" y="22" width="3" height="2" fill="var(--icon)"/></svg>
    <span style="left:52px">********</span>
  </div>
  <div class="field field--password" style="left:20px;top:283px;width:263px">
    <svg width="20" height="26" viewBox="0 0 20 26"><circle cx="10" cy="7" r="6" fill="var(--icon)"/><circle cx="10" cy="6" r="2" fill="var(--field)"/><rect x="8" y="12" width="4" height="13" fill="var(--icon)"/><rect x="12" y="18" width="3" height="2" fill="var(--icon)"/><rect x="12" y="22" width="3" height="2" fill="var(--icon)"/></svg>
    <span style="left:52px">********</span>
  </div>
  <svg class="check" style="left:240px;top:225px" viewBox="0 0 64 64" role="img" aria-label="Submit">
    <circle cx="32" cy="32" r="31" fill="var(--check-ring)"/><circle cx="32" cy="32" r="24" fill="var(--check-core)"/>
    <path d="M20 33 L29 42 L45 21" fill="none" stroke="var(--check-tick)" stroke-width="6" stroke-linecap="round" stroke-linejoin="round"/>
  </svg>
  <div class="social-login" style="left:57px;top:405px"><i class="mark"></i><span>Login with Chatterly</span></div>
</section>

</body>
</html>
```